CONTACT US Page and design for website

We need a contact us page for our website. We would like it to have a message area, a map, our information, etc.

Please see the text attachment for what we are looking for. We need to have something that is creative and interesting, modern and professional.

We believe that a contact US page should be very creative because everyone clicks that to contact us. We want it to be super professional, attention grabbing, pleasing to the eye.

PLEASE KEEP THE HEADER AND FOOTER THE SAME, ONLY THE ACTUAL CONTACT US PAGE NEEDS TO BE WORKED ON. THANKS!
We are excited to work with designers for this project.

Target Market(s)

Clients in technology business

Industry/Entity Type

Information Technology

Number of Pages Required

1 page

Font styles to use
Serif

Requirements
Must have
• CHECK THE TEXT ATTACHMENT PLEASE
• Must stay within our design colors and theme.
Nice to have
• see attachment
Should not have
• it should be special

```html
<!DOCTYPE html>
<html lang="en">
<head>
<meta charset="utf-8">
<title>Contact Us – Nordvale Systems</title>
<link href="https://fonts.googleapis.com/css2?family=Arimo:wght@400;700&display=swap" rel="stylesheet">
<style>
:root{
  --teal:#36b9b0;
  --ink:#222;
  --text:#333;
  --muted:#666;
  --line:#d8d8d8;
  --band:#f5f5f5;
  --footer:#a4a4a4;
  --footer-dark:#989898;
  --white:#fff;
  --map:#e8e8e8;
}
*{box-sizing:border-box;margin:0;padding:0}
html,body{width:978px;height:1200px;overflow:hidden;background:var(--white);font-family:"Arimo",Arial,sans-serif;color:var(--text)}
.page{position:relative;width:978px;height:1200px}
.abs{position:absolute}

/* header */
.brand{left:51px;top:14px;display:flex;align-items:center;gap:10px}
.brand-mark{width:40px;height:40px;background:var(--teal);border-radius:50%}
.brand-name{font-size:24px;color:var(--teal);font-weight:400;letter-spacing:2px}
.account{right:50px;top:0;width:138px;height:24px;background:#9a9a9a;border-radius:0 0 18px 18px;display:flex;font-size:8px;color:#eee}
.account span{flex:1;display:flex;align-items:center;justify-content:center}
.account span+span{background:#8a8a8a;border-radius:0 0 18px 0}
.contact-top{right:50px;top:33px;display:flex;align-items:center;gap:10px;font-size:10px;color:var(--text)}
.round{width:30px;height:30px;border:1px solid var(--line);border-radius:50%;display:flex;align-items:center;justify-content:center}
.contact-top .phone{font-size:14px}
.nav{left:0;top:72px;width:978px;height:37px;border-top:1px solid #e6e6e6;border-bottom:1px solid var(--teal)}
.nav ul{list-style:none;display:flex;position:absolute;left:58px;top:13px;gap:19px;font-size:9px;color:#444}
.search{right:94px;top:8px;width:132px;height:23px;border:1px solid #bbb;border-radius:12px;font-size:8px;padding:7px 16px;color:#333}
.search svg{position:absolute;right:8px;top:6px}
.cart{right:57px;top:6px;width:27px;height:27px;border:1px solid #bbb;border-radius:50%;display:flex;align-items:center;justify-content:center}

/* form band */
.band{left:0;top:109px;width:978px;height:122px;background:var(--band)}
.band h1{position:absolute;width:100%;top:28px;text-align:center;font-size:21px;font-weight:400;color:var(--ink)}
.field{position:absolute;top:61px;height:31px;background:var(--white);border:1px solid #ddd;font-size:8px;color:#555;padding:12px 15px}
.submit{position:absolute;top:61px;left:878px;width:50px;height:31px;background:#222;color:#fff;font-size:8px;display:flex;align-items:center;justify-content:center}

/* info column */
.info{left:51px;top:266px;width:190px}
.info h2{font-size:12.5px;font-weight:400;color:var(--teal);margin-bottom:5px}
.info p,.info li{font-size:7.5px;line-height:1.35;color:var(--text)}
.info .blk{margin-bottom:26px}
.row{display:flex;gap:8px;align-items:flex-start;margin-bottom:11px}
.row .ic{width:9px;flex:none}
.indent{padding-left:16px}
.label{font-size:7.5px;margin:6px 0 6px}
.gap{margin-top:16px}

.map{left:243px;top:268px;width:685px;height:558px;background:linear-gradient(135deg,#ececec,#e2e2e2)}
.pin{left:289px;top:262px;font-size:10px;color:#b21f1f;font-weight:700;display:flex;align-items:flex-end;gap:6px}

/* footer */
.footer{left:0;top:878px;width:978px;height:204px;background:var(--footer);color:var(--white)}
.about{position:absolute;left:290px;top:12px;width:400px;text-align:center;font-size:10.5px;line-height:1.4}
.fdiv{position:absolute;left:297px;top:77px;width:454px;height:1px;background:#b8b8b8}
.fcontact{position:absolute;top:93px;display:flex;gap:6px;font-size:10.5px;line-height:1.4}
.flinks{position:absolute;top:140px;left:245px;display:flex;gap:29px;font-size:12px}
.support{position:absolute;left:632px;top:140px;text-align:center}
.support small{display:block;font-size:7px;line-height:1.45}
.sub{left:0;top:1082px;width:978px;height:118px;background:var(--footer-dark);color:var(--white)}
.socials{position:absolute;left:411px;top:14px;display:flex;gap:10px}
.socials span{width:28px;height:28px;border:1px solid #ccc;border-radius:50%;display:flex;align-items:center;justify-content:center}
.socials span i{width:6px;height:6px;background:#ddd;border-radius:50%}
.subline{position:absolute;left:145px;top:57px;width:720px;height:1px;background:#aaa}
.copy{position:absolute;left:447px;top:68px;display:flex;gap:6px;align-items:center;font-size:9.5px;line-height:1.4}
.copy b{width:16px;height:16px;background:#ddd;display:block}
.tag{position:absolute;right:20px;top:77px;font-size:7px}
.tab{width:152px;height:19px;background:var(--teal);color:#fff;font-size:10px;font-weight:700;padding:4px 7px;border:1px solid #fff;display:flex;justify-content:space-between}
</style>
</head>
<body>
<div class="page">

  <header>
    <div class="abs brand"><span class="brand-mark"></span><span class="brand-name">NORDVALE SYSTEMS</span></div>
    <div class="abs account"><span>SIGN UP</span><span>LOGIN</span></div>
    <div class="abs contact-top">
      <span class="round"><svg width="12" height="10" viewBox="0 0 12 10"><ellipse cx="6" cy="4.5" rx="5" ry="3.6" fill="#666"/></svg></span>
      <span>LIVE CHAT</span>
      <span class="round"><svg width="11" height="11" viewBox="0 0 24 24"><path d="M6.6 10.8a15 15 0 0 0 6.6 6.6l2.2-2.2c.3-.3.7-.4 1-.2 1.1.4 2.3.6 3.6.6.6 0 1 .4 1 1V20c0 .6-.4 1-1 1A17 17 0 0 1 3 4c0-.6.4-1 1-1h3.5c.6 0 1 .4 1 1 0 1.3.2 2.5.6 3.6.1.3 0 .7-.2 1z" fill="#36b9b0"/></svg></span>
      <span class="phone">555-014-2200</span>
    </div>
    <nav class="abs nav">
      <ul><li>SERVERS</li><li>WORKSTATIONS</li><li>COMPONENTS</li><li>VIRTUAL REALITY</li><li>DRONES</li><li>ABOUT US</li><li>BLOG</li><li>RESOURCES</li><li>CONTACT US</li></ul>
      <div class="abs search">Search<svg width="10" height="10" viewBox="0 0 10 10"><circle cx="4" cy="4" r="3" fill="none" stroke="#36b9b0" stroke-width="1.4"/><path d="M6.2 6.2 9 9" stroke="#36b9b0" stroke-width="1.6"/></svg></div>
      <div class="abs cart"><svg width="12" height="10" viewBox="0 0 12 10"><path d="M1 2h10l-1.5 7h-7z" fill="#36b9b0"/></svg></div>
    </nav>
  </header>

  <section class="abs band">
    <h1>CONTACT US</h1>
    <div class="field" style="left:51px;width:163px">Name</div>
    <div class="field" style="left:219px;width:163px">E-mail</div>
    <div class="field" style="left:387px;width:163px">Phone Number</div>
    <div class="field" style="left:555px;width:317px">Message</div>
    <div class="submit">SUBMIT</div>
  </section>

  <aside class="abs info">
    <div class="blk">
      <h2>OFFICE HEADQUARTERS</h2>
      <div class="row"><svg class="ic" viewBox="0 0 10 12"><path d="M5 0a4 4 0 0 0-4 4c0 3 4 8 4 8s4-5 4-8a4 4 0 0 0-4-4z" fill="#777"/><circle cx="5" cy="4" r="1.5" fill="#fff"/></svg><p>Nordvale Systems, LLC.<br>4820 Larkin Ave. Westbrook, CA 91400</p></div>
    </div>
    <div class="blk" style="margin-top:-8px">
      <h2>HOURS OF OPERATION</h2>
      <div class="row" style="margin-bottom:10px"><svg class="ic" viewBox="0 0 10 10"><circle cx="5" cy="5" r="4" fill="none" stroke="#777"/><path d="M5 2.5V5h2" stroke="#777" fill="none"/></svg><p>Monday: 8:00am- 5:00pm</p></div>
      <p class="indent" style="margin-bottom:11px">Tuesday:8:00am- 5:00pm</p>
      <p class="indent" style="margin-bottom:11px">Wednesday: 8:00am- 5:00pm</p>
      <p class="indent" style="margin-bottom:11px">Thursday: 8:00am- 5:00pm</p>
      <p class="indent" style="margin-bottom:11px">Friday: 8:00am- 5:00pm</p>
      <p class="indent">Our dedicated customer service representatives are available 24/7 by phone.</p>
    </div>
    <div class="blk" style="margin-top:-6px">
      <h2 style="margin-bottom:11px">STAY CONNECTED</h2>
      <div class="row"><span class="ic" style="height:8px;background:#777;border-radius:1px"></span><p>Friendwall</p></div>
      <div class="row"><span class="ic" style="height:8px;background:#777;border-radius:1px"></span><p>Worklink</p></div>
      <div class="row"><span class="ic" style="height:8px;background:#777;border-radius:50%"></span><p>Circleplus</p></div>
      <div class="row"><span class="ic" style="height:8px;background:#777;border-radius:1px"></span><p>Snapgram</p></div>
    </div>
    <div class="blk" style="margin-top:-10px">
      <h2>CONTACT INFO</h2>
      <p class="label">General Inquiries</p>
      <div class="row"><svg class="ic" viewBox="0 0 24 24"><path d="M6.6 10.8a15 15 0 0 0 6.6 6.6l2.2-2.2c.3-.3.7-.4 1-.2 1.1.4 2.3.6 3.6.6.6 0 1 .4 1 1V20c0 .6-.4 1-1 1A17 17 0 0 1 3 4c0-.6.4-1 1-1h3.5c.6 0 1 .4 1 1 0 1.3.2 2.5.6 3.6.1.3 0 .7-.2 1z" fill="#777"/></svg><p>(555)014-2200</p></div>
      <div class="row"><svg class="ic" viewBox="0 0 10 8"><rect width="10" height="8" fill="#777"/><path d="M0 0l5 4 5-4" stroke="#fff" fill="none"/></svg><p>info@nordvale.example</p></div>
      <p class="label gap">Sales Inquiries</p>
      <div class="row"><svg class="ic" viewBox="0 0 24 24"><path d="M6.6 10.8a15 15 0 0 0 6.6 6.6l2.2-2.2c.3-.3.7-.4 1-.2 1.1.4 2.3.6 3.6.6.6 0 1 .4 1 1V20c0 .6-.4 1-1 1A17 17 0 0 1 3 4c0-.6.4-1 1-1h3.5c.6 0 1 .4 1 1 0 1.3.2 2.5.6 3.6.1.3 0 .7-.2 1z" fill="#777"/></svg><p>(555)014-2200</p></div>
      <div class="row"><svg class="ic" viewBox="0 0 10 8"><rect width="10" height="8" fill="#777"/><path d="M0 0l5 4 5-4" stroke="#fff" fill="none"/></svg><p>sales@nordvale.example</p></div>
      <p class="label gap">Purchasing Inquiries</p>
      <div class="row"><svg class="ic" viewBox="0 0 24 24"><path d="M6.6 10.8a15 15 0 0 0 6.6 6.6l2.2-2.2c.3-.3.7-.4 1-.2 1.1.4 2.3.6 3.6.6.6 0 1 .4 1 1V20c0 .6-.4 1-1 1A17 17 0 0 1 3 4c0-.6.4-1 1-1h3.5c.6 0 1 .4 1 1 0 1.3.2 2.5.6 3.6.1.3 0 .7-.2 1z" fill="#777"/></svg><p>(555)014-2201</p></div>
      <div class="row"><svg class="ic" viewBox="0 0 10 8"><rect width="10" height="8" fill="#777"/><path d="M0 0l5 4 5-4" stroke="#fff" fill="none"/></svg><p>purchasing@nordvale.example</p></div>
    </div>
  </aside>

  <div class="abs map" role="img" aria-label="Street map of the area around the office, with a red pin marking 4820 Larkin Avenue"></div>

  <footer>
    <div class="abs footer">
      <p class="about">Based in Westbrook California, Nordvale Systems offers custom servers, storage, and workstations for local businesses in Los Angeles, Beverly Hills, Thousand Oaks, Ventura, Orange County, Santa Barbara, Oxnard, Irvine, Anaheim, and San Diego. Nordvale Systems also offers such products to clients throughout the United States and Worldwide.</p>
      <div class="fdiv"></div>
      <div class="fcontact" style="left:296px"><svg width="9" height="11" viewBox="0 0 10 12"><path d="M5 0a4 4 0 0 0-4 4c0 3 4 8 4 8s4-5 4-8a4 4 0 0 0-4-4z" fill="#fff"/></svg><span>4820 Larkin Ave.<br>Westbrook, CA 91400</span></div>
      <div class="fcontact" style="left:447px"><svg width="10" height="10" viewBox="0 0 24 24"><path d="M6.6 10.8a15 15 0 0 0 6.6 6.6l2.2-2.2c.3-.3.7-.4 1-.2 1.1.4 2.3.6 3.6.6.6 0 1 .4 1 1V20c0 .6-.4 1-1 1A17 17 0 0 1 3 4c0-.6.4-1 1-1h3.5c.6 0 1 .4 1 1 0 1.3.2 2.5.6 3.6.1.3 0 .7-.2 1z" fill="#fff"/></svg><span>555-014-2200</span></div>
      <div class="fcontact" style="left:579px"><svg width="11" height="9" viewBox="0 0 10 8"><rect width="10" height="8" fill="#fff"/><path d="M0 0l5 4 5-4" stroke="#a4a4a4" fill="none"/></svg><span>sales@nordvale.example</span></div>
      <div class="flinks"><span>Computer Hardware</span><span>Drones</span><span>Virtual Reality</span><span>About Us</span></div>
      <div class="support"><span style="font-size:12px">Customer Support</span><small style="margin-top:2px">Terms and Conditions</small><small>Warranty Information</small><small>Contact Us</small><small>Return Policy</small></div>
    </div>
    <div class="abs sub">
      <div class="socials"><span><i></i></span><span><i></i></span><span><i></i></span><span><i></i></span></div>
      <div class="subline"></div>
      <div class="copy"><b></b><span>Nordvale Systems, LLC.<br>Copyright © 2017</span></div>
      <span class="tag">M2</span>
    </div>
    <div class="abs tab" style="left:814px;top:871px">Leave a message <span>⌃</span></div>
    <div class="abs tab" style="left:814px;top:1181px">Leave a message <span>⌃</span></div>
  </footer>

</div>
</body>
</html>
```